Modern, Clean website for painting service.

We are working with a company called Brushwell Crafts and building a new website for them.

Some sites to use for content/competitors and inspiration:

https://www.coatvantaged.com
https://ridgeline-hue.com
https://tedvarnokcoating.com

Thank you for taking the time to consider designing a website for us. We are web developers based in Stockton, CA, USA. Most of our projects go through the same process. Understanding this process may help you win a project with us. We custom-code all of our websites in-house. We don’t have any requirements as to what tools you use for your design, but we prefer Figma files. For any design that we label as four-stars, we send it to the client for review. The client picks the final design they want us to use. Once we complete this process, we will continue to show additional clients all the four-star sites and purchase them later. Your designs will have multiple chances to sell. For better chances of success, we ask that you follow these guidelines.

IMAGES:
If you use any images or icons in the design, we ask that you have a link to the asset so we can purchase the image/icon. Most of the designs we submit do not have the customer’s images on them unless they have some great images. Be creative; show us the feeling you are trying to portray with your image choices. Use any royalty-free site you choose. We subscribe to Kelvra and mainly use their images, but we can purchase images outside of Kelvra. PLEASE NOTE: we will not submit designs to clients with watermarks on the images.

FONTS:
We ask that you identify the fonts used in the design. This can be done in a message if you want. We typically use Google Fonts and Kelvra Type.

CONTENT:
We're always open to different content and ideas. We often submit designs with stock images so the client can see our vision. We typically take pictures after the website launch to use their images with our vision. Lorem Ipsum is fine for paragraphs, but we ask that you write the headers in correct English. We want to be able to show the vision and identify the sections of the website.

INSPIRATION:
We typically add a couple of links in the brief of websites we like to help you get started in your design.

REVISIONS:
We do not often ask for revisions of the designs unless we see something in the design that may not appeal to the client. If there are slight changes that we want to make, we do that in the development process.

FEEDBACK:
We rarely give feedback on designs during the design process. We are working on many website projects and do not have the time to provide feedback. We usually respond if your request is well thought out and asks specific questions, but a note asking “feedback, please” usually goes unanswered.

```html
<!DOCTYPE html>
<html lang="en">
<head>
<meta charset="UTF-8">
<title>Brushwell Crafts – House Painting Services</title>
<link rel="stylesheet" href="https://fonts.googleapis.com/css2?family=Jost:wght@400;500;600;700&family=Poppins:wght@300;400;500&display=swap">
<style>
:root{
  --navy:#141c45;
  --navy-deep:#0d1530;
  --crimson:#a3001f;
  --wine:#8c0a24;
  --ink:#111111;
  --text:#555a66;
  --card:#f5f5f6;
  --field:#f2f2f4;
  --white:#ffffff;
  --brand-grad:linear-gradient(90deg,var(--navy) 0%,#5a1240 50%,var(--crimson) 100%);
}
*{margin:0;padding:0;box-sizing:border-box}
html,body{width:1200px;height:4744px;overflow:hidden}
body{position:relative;background:var(--white);font-family:"Poppins",sans-serif;color:var(--ink)}
.abs{position:absolute}
.heading{font-family:"Jost",sans-serif}

/* top bar */
.topbar{left:0;top:0;width:1200px;height:41px;background:var(--brand-grad);color:var(--white);font-size:15px}
.topbar .address{left:44px;top:11px;display:flex;align-items:center;gap:10px}
.topbar .email{left:762px;top:9px;display:flex;align-items:center;gap:10px}
.topbar .social{top:13px;width:15px;height:15px;border-radius:50%;background:var(--white)}

/* nav */
.nav{left:0;top:41px;width:1200px;height:97px;background:var(--white)}
.nav a{position:absolute;top:42px;font-size:19px;color:var(--ink);text-decoration:none;font-family:"Poppins",sans-serif}
.nav .btn-contact{left:992px;top:35px;width:153px;height:40px;border-radius:20px;background:var(--brand-grad);color:var(--white);font-size:16px;display:flex;align-items:center;justify-content:center}
.logo-badge{left:491px;top:138px;width:182px;height:78px;z-index:5}
.brand-mark{left:491px;top:88px;width:182px;text-align:center;z-index:6;font-family:"Jost",sans-serif;font-weight:500;font-size:22px;line-height:1.15;color:var(--crimson);letter-spacing:1px}
.brand-mark .dot{display:inline-block;width:12px;height:12px;background:var(--crimson);margin-right:6px}

/* hero */
.hero{left:0;top:138px;width:1200px;height:800px}
.hero-eyebrow{left:0;top:338px;width:1180px;text-align:center;font-size:11px;font-weight:700;color:var(--navy);letter-spacing:.2px}
.hero-title{left:0;top:358px;width:1170px;text-align:center;font-size:80px;font-weight:600;line-height:98px;color:var(--white)}
.hero-text{left:270px;top:582px;width:630px;text-align:center;font-size:18px;line-height:24px;color:var(--white)}
.btn-hero{left:484px;top:703px;width:199px;height:37px;border-radius:19px;background:var(--brand-grad);color:var(--white);font-size:17px;font-family:"Jost",sans-serif;display:flex;align-items:center;justify-content:center}

/* about */
.about-hex{left:55px;top:1003px;width:416px;height:474px}
.about-title{left:567px;top:1050px;width:600px;font-size:62px;font-weight:600;line-height:78px;color:var(--navy)}
.about-text{left:573px;width:530px;font-size:14.5px;line-height:20px;color:var(--text)}
.btn-dark{left:571px;top:1398px;width:261px;height:52px;border-radius:26px;background:var(--brand-grad);color:var(--white);font-family:"Jost",sans-serif;font-size:23px;display:flex;align-items:center;justify-content:center}

/* features */
.feature{top:1570px;width:307px;height:191px;background:var(--card);text-align:center}
.feature::after{content:"";position:absolute;left:-4px;right:-2px;bottom:-3px;height:5px;background:var(--brand-grad)}
.feature svg{margin-top:18px}
.feature h3{font-family:"Jost",sans-serif;font-weight:500;font-size:31px;margin-top:6px;color:var(--ink)}

/* services */
.services{left:0;top:1881px;width:1200px;height:747px;background:var(--brand-grad)}
.services h2{position:absolute;left:0;top:70px;width:1190px;text-align:center;font-size:62px;font-weight:600;color:var(--white)}
.service-photo{top:240px;width:264px;height:264px;border-radius:50%}
.service-name{top:538px;width:360px;text-align:center;font-family:"Jost",sans-serif;font-weight:500;font-size:29px;color:var(--white)}
.btn-light{left:473px;top:655px;width:260px;height:52px;border-radius:26px;background:var(--white);color:var(--crimson);font-family:"Jost",sans-serif;font-weight:500;font-size:24px;display:flex;align-items:center;justify-content:center}

/* work */
.section-title{left:0;width:1230px;text-align:center;font-size:66px;font-weight:600;color:var(--ink);text-transform:uppercase}
.work-grid{left:83px;top:2875px;width:1029px;height:438px;display:grid;grid-template-columns:repeat(3,1fr);grid-template-rows:repeat(2,1fr)}

/* quote */
.contact-card{left:83px;width:313px;height:84px;background:var(--white);box-shadow:0 2px 8px rgba(0,0,0,.08);display:flex;align-items:center;gap:18px;padding-left:24px}
.contact-card .ico{width:38px;height:38px;border-radius:50%;background:var(--brand-grad);display:flex;align-items:center;justify-content:center}
.contact-card .label{font-size:13px;font-weight:500;color:var(--ink);line-height:16px}
.contact-card .value{font-size:20px;color:var(--text);line-height:22px}
.field{height:37px;background:var(--field);font-size:13px;color:#666;padding:10px 16px}
.btn-submit{left:447px;top:3865px;width:663px;height:51px;border-radius:26px;background:var(--wine);color:var(--white);font-family:"Jost",sans-serif;font-weight:600;font-size:23px;display:flex;align-items:center;justify-content:center}

/* footer */
.footer{left:0;top:4040px;width:1200px;height:704px}
.footer-brand{left:0;top:180px;width:1200px;text-align:center;font-family:"Jost",sans-serif;font-weight:500;font-size:46px;letter-spacing:3px;color:var(--white)}
.footer-brand .dot{display:inline-block;width:22px;height:22px;background:var(--crimson);margin-right:14px;vertical-align:middle}
.footer-nav{top:370px;font-family:"Jost",sans-serif;font-size:29px;color:var(--white)}
.footer-social{top:460px;width:34px;height:34px;border-radius:50%;background:var(--crimson)}
.footer-legal{left:0;top:570px;width:1230px;text-align:center;font-size:20px;color:var(--white)}
.footer-copy{left:0;top:628px;width:1230px;text-align:center;font-size:12px;color:var(--white)}
</style>
</head>
<body>

<!-- top bar -->
<div class="abs topbar">
  <div class="abs address">
    <svg width="14" height="18" viewBox="0 0 14 18"><path d="M7 0C3.1 0 0 3.1 0 7c0 5 7 11 7 11s7-6 7-11C14 3.1 10.9 0 7 0z" fill="#fff"/><circle cx="7" cy="7" r="2.6" fill="#2a1e4c"/></svg>
    <span>Your Address Here</span>
  </div>
  <div class="abs email">
    <svg width="18" height="13" viewBox="0 0 18 13"><rect width="18" height="13" rx="1.5" fill="#fff"/><path d="M1 1l8 6 8-6" stroke="#5a1240" stroke-width="1.5" fill="none"/></svg>
    <span>info@website.com</span>
  </div>
  <div class="abs social" style="left:1007px"></div>
  <div class="abs social" style="left:1060px"></div>
  <div class="abs social" style="left:1115px"></div>
</div>

<!-- navigation -->
<nav class="abs nav">
  <a style="left:52px">Home</a>
  <a style="left:160px">About</a>
  <a style="left:262px">Services</a>
  <a style="left:382px">Gallery</a>
  <a style="left:716px">Reviews</a>
  <a style="left:837px">Blog</a>
  <a class="btn-contact">Contact Now</a>
</nav>
<svg class="abs logo-badge" viewBox="0 0 182 78"><polygon points="0,0 182,0 182,44 91,78 0,44" fill="#fff"/></svg>
<div class="abs brand-mark"><span class="dot"></span>BRUSHWELL<br>CRAFTS</div>

<!-- hero -->
<section class="abs hero">
  <svg width="1200" height="800" viewBox="0 0 1200 800" role="img" aria-label="Bright white living room interior with staircase, freshly painted walls">
    <defs>
      <linearGradient id="heroPhoto" x1="0" y1="0" x2="1" y2="1">
        <stop offset="0" stop-color="#3d3a37"/>
        <stop offset=".5" stop-color="#6b6660"/>
        <stop offset="1" stop-color="#4a4640"/>
      </linearGradient>
      <linearGradient id="brandBand" x1="0" y1="0" x2="1" y2="0">
        <stop offset="0" stop-color="#141c45"/>
        <stop offset=".5" stop-color="#4a1540"/>
        <stop offset="1" stop-color="#a3001f"/>
      </linearGradient>
    </defs>
    <polygon points="0,0 1200,0 1200,589 590,778 0,598" fill="url(#heroPhoto)"/>
    <polygon points="0,598 590,778 1200,589 1200,630 590,792 0,606" fill="url(#brandBand)"/>
  </svg>
</section>
<div class="abs hero-eyebrow">HIGH QUALITY PAINT SOLUTION</div>
<h1 class="abs heading hero-title">House Painting<br>Services</h1>
<p class="abs hero-text">Lorem ipsum dolor sit amet, consectetur adipiscing elit, sed do<br>eiusmod temporincididunt ut labore et dolore magna aliqua.<br>Ut enim ad minim veniam</p>
<div class="abs btn-hero">GET A FREE QUOTE</div>

<!-- about -->
<svg class="abs about-hex" viewBox="0 0 416 474" role="img" aria-label="White paint being poured from a can into a tray">
  <defs>
    <linearGradient id="hexBorder" x1="0" y1="0" x2="1" y2="1">
      <stop offset="0" stop-color="#141c45"/><stop offset="1" stop-color="#a3001f"/>
    </linearGradient>
    <linearGradient id="hexPhoto" x1="0" y1="0" x2="1" y2="1">
      <stop offset="0" stop-color="#8a8e99"/><stop offset=".45" stop-color="#e59a84"/><stop offset="1" stop-color="#e8dcd2"/>
    </linearGradient>
  </defs>
  <polygon points="208,0 412,118 412,355 208,474 4,355 4,118" fill="url(#hexBorder)"/>
  <polygon points="208,14 400,125 400,348 208,460 16,348 16,125" fill="url(#hexPhoto)"/>
</svg>
<h2 class="abs heading about-title">The Best Choice<br>For Tree Services</h2>
<p class="abs about-text" style="top:1222px">Lorem ipsum dolor sit amet, consectetur adipiscing elit, sed do eiusmod tempor incididunt ut labore et dolore magna aliqua. Ut enim ad minim veniam, quis nostrud exercitation ullamco.</p>
<p class="abs about-text" style="top:1303px">Lorem ipsum dolor sit amet, consectetur adipiscing elit, sed do eiusmod tempor incididunt ut labore et dolore magna aliqua. Ut enim ad minim veniam, quis nostrud exercitation ullamco.</p>
<div class="abs btn-dark">GET A FREE QUOTE</div>

<!-- features -->
<div class="abs feature" style="left:52px">
  <svg width="80" height="90" viewBox="0 0 80 90" fill="none" stroke="#a3001f" stroke-width="3">
    <rect x="8" y="6" width="52" height="18" rx="3"/><path d="M60 15h10v20H36v12"/><rect x="31" y="47" width="10" height="38" rx="4"/>
  </svg>
  <h3>Quality Finish</h3>
</div>
<div class="abs feature" style="left:449px">
  <svg width="80" height="90" viewBox="0 0 80 90" fill="none" stroke="#a3001f" stroke-width="3">
    <path d="M6 44L40 14l34 30"/><path d="M14 38v44h52V38"/><rect x="32" y="56" width="16" height="26"/><rect x="54" y="14" width="8" height="16"/>
  </svg>
  <h3>Best Support</h3>
</div>
<div class="abs feature" style="left:845px">
  <svg width="80" height="90" viewBox="0 0 80 90" fill="none" stroke="#a3001f" stroke-width="3">
    <path d="M30 20h20l14 40-26 22-26-22z"/><circle cx="40" cy="30" r="4"/><path d="M40 10v16"/><circle cx="38" cy="54" r="11"/><path d="M38 47v14"/>
  </svg>
  <h3>Better Price</h3>
</div>

<!-- services -->
<section class="abs services">
  <h2 class="heading">Our Services</h2>
  <div class="abs service-photo" style="left:67px;background:linear-gradient(135deg,#5fa048 0%,#c9c1a8 55%,#4a8fb8 100%)" role="img" aria-label="Painters in hard hats painting an exterior wall"></div>
  <div class="abs service-photo" style="left:470px;background:linear-gradient(135deg,#9cc3d8 0%,#dfe9ef 50%,#5b8a9e 100%)" role="img" aria-label="Worker drilling into a commercial wall"></div>
  <div class="abs service-photo" style="left:873px;background:linear-gradient(135deg,#9e9488 0%,#8a2a12 55%,#d08a4c 100%)" role="img" aria-label="Brush applying stain to a wooden plank"></div>
  <div class="abs service-name" style="left:17px">Residential Projects</div>
  <div class="abs service-name" style="left:431px">Commercial Projects</div>
  <div class="abs service-name" style="left:826px">Restoration Projects</div>
  <div class="abs btn-light">VIEW ALL SERVICES</div>
</section>

<!-- recent work -->
<h2 class="abs heading section-title" style="top:2722px">Recent Work</h2>
<div class="abs work-grid">
  <div style="background:linear-gradient(160deg,#f1ece4,#c4a57a)" role="img" aria-label="Cosy living room with fireplace and sofas"></div>
  <div style="background:linear-gradient(180deg,#2a4a94,#1d3570)" role="img" aria-label="Blue painted wall above a blue sofa"></div>
  <div style="background:linear-gradient(180deg,#e0a83a,#d8c8a8)" role="img" aria-label="Mustard yellow wall with shelf and armchair"></div>
  <div style="background:linear-gradient(180deg,#4f8fd6,#e7e3df)" role="img" aria-label="House facade with red trimmed gables"></div>
  <div style="background:linear-gradient(90deg,#e8e8e4,#6a3420 40%,#5a7a32)" role="img" aria-label="Freshly stained wooden fence beside a brick post"></div>
  <div style="background:linear-gradient(160deg,#e6ebf0,#2e55a8)" role="img" aria-label="Blue corrugated commercial building"></div>
</div>

<!-- get a quote -->
<h2 class="abs heading section-title" style="top:3476px">Get A Quote</h2>
<div class="abs contact-card" style="top:3603px">
  <div class="ico"><svg width="18" height="18" viewBox="0 0 24 24"><path d="M6.6 10.8a15 15 0 006.6 6.6l2.2-2.2c.3-.3.7-.4 1-.2 1.1.4 2.3.6 3.6.6.6 0 1 .4 1 1V20c0 .6-.4 1-1 1A17 17 0 013 4c0-.6.4-1 1-1h3.5c.6 0 1 .4 1 1 0 1.3.2 2.5.6 3.6.1.3 0 .7-.2 1z" fill="#fff"/></svg></div>
  <div><div class="label">CALL US</div><div class="value">888 888 8888</div></div>
</div>
<div class="abs contact-card" style="top:3721px">
  <div class="ico"><svg width="18" height="14" viewBox="0 0 18 13"><rect width="18" height="13" rx="1.5" fill="#fff"/><path d="M1 1l8 6 8-6" stroke="#7a0c2c" stroke-width="1.5" fill="none"/></svg></div>
  <div><div class="label">SEND AN EMAIL</div><div class="value">info@website.com</div></div>
</div>
<div class="abs contact-card" style="top:3837px">
  <div class="ico"><svg width="14" height="18" viewBox="0 0 14 18"><path d="M7 0C3.1 0 0 3.1 0 7c0 5 7 11 7 11s7-6 7-11C14 3.1 10.9 0 7 0z" fill="#fff"/><circle cx="7" cy="7" r="2.6" fill="#7a0c2c"/></svg></div>
  <div><div class="label">LOCATION</div><div class="value">Your Address Here</div></div>
</div>
<div class="abs field" style="left:449px;top:3607px;width:313px">Your Name</div>
<div class="abs field" style="left:795px;top:3607px;width:315px">Your Phone</div>
<div class="abs field" style="left:449px;top:3680px;width:313px">Email Address</div>
<div class="abs field" style="left:795px;top:3680px;width:315px">Select Service</div>
<div class="abs field" style="left:447px;top:3754px;width:663px;height:81px">Additional Message</div>
<div class="abs btn-submit">GET A FREE QUOTE NOW</div>

<!-- footer -->
<footer class="abs footer">
  <svg class="abs" style="left:0;top:0" width="1200" height="704" viewBox="0 0 1200 704" role="img" aria-label="Hand holding a paint roller on a dark background">
    <defs>
      <linearGradient id="footBand" x1="0" y1="0" x2="1" y2="0">
        <stop offset="0" stop-color="#141c45"/><stop offset=".5" stop-color="#5a1240"/><stop offset="1" stop-color="#a3001f"/>
      </linearGradient>
      <linearGradient id="footPhoto" x1="0" y1="0" x2="1" y2="1">
        <stop offset="0" stop-color="#1a2436"/><stop offset=".5" stop-color="#24324a"/><stop offset="1" stop-color="#0a1020"/>
      </linearGradient>
    </defs>
    <polygon points="0,174 616,14 1200,184 1200,704 0,704" fill="url(#footBand)"/>
    <polygon points="0,182 616,26 1200,196 1200,704 0,704" fill="url(#footPhoto)"/>
  </svg>
  <div class="abs footer-brand"><span class="dot"></span>BRUSHWELL CRAFTS</div>
  <span class="abs footer-nav" style="left:166px">Home</span>
  <span class="abs footer-nav" style="left:324px">About</span>
  <span class="abs footer-nav" style="left:474px">Services</span>
  <span class="abs footer-nav" style="left:650px">Gallery</span>
  <span class="abs footer-nav" style="left:826px">Reviews</span>
  <span class="abs footer-nav" style="left:1000px">Blog</span>
  <div class="abs footer-social" style="left:475px"></div>
  <div class="abs footer-social" style="left:598px"></div>
  <div class="abs footer-social" style="left:727px"></div>
  <div class="abs footer-legal">Privacy Policy | Terms &amp; Conditions</div>
  <div class="abs footer-copy">Copyright 2024 Brushwell Crafts. All Rights Reserved.</div>
</footer>

</body>
</html>
```